Pop-up Banner

Would like a design for a pop-up 85 x 206cm banner for a trade show. (from norla press)
We would like "our logo" (brightwave holdings) - then the tagline - "Your Trusted Partner in Data-Driven Decisions"
*Supporting Bullets*
Unified data, analytics & AI
Trusted insights, faster outcomes
Real-time intelligence at scale
Enterprise-ready, secure solutions
Clarity from data complexity
trusted by...some company logos
Partners with : partner logo
Our Colours: #FFA300, #3D4176, #FDD16E, #F87C57, #A68118, #1C2F36

```html
<!DOCTYPE html>
<html lang="en">
<head>
<meta charset="utf-8">
<title>Brightwave Holdings – Pop-up Banner</title>
<link rel="stylesheet" href="https://fonts.googleapis.com/css2?family=Bebas+Neue&family=Oswald:wght@200&family=Poppins:wght@400;600;700;800&display=swap">
<style>
  :root {
    --orange: #FFA300;
    --indigo: #3D4176;
    --gold: #FDD16E;
    --coral: #F87C57;
    --ochre: #A68118;
    --ink: #1C2F36;
    --white: #ffffff;
    --stage: #b3b3b3;
  }
  * { margin: 0; padding: 0; box-sizing: border-box; }
  html, body { width: 1200px; height: 2547px; overflow: hidden; }
  body { background: var(--stage); position: relative; font-family: "Poppins", sans-serif; }

  .banner {
    position: absolute; left: 127px; top: 125px;
    width: 947px; height: 2297px;
    background: var(--white); overflow: hidden;
  }
  .abs { position: absolute; }

  /* brand header */
  .brand-mark {
    left: 178px; top: 96px; width: 140px; height: 140px;
    border-radius: 50%; background: var(--orange);
  }
  .brand-name {
    left: 375px; top: 100px;
    font-family: "Poppins", sans-serif; font-weight: 700;
    font-size: 58px; line-height: 64px; letter-spacing: 2px;
    color: var(--orange); text-transform: uppercase;
  }

  /* headline bands */
  .band-dark { left: 0; top: 322px; width: 947px; height: 424px; background: var(--ink); }
  .band-gap { left: 0; top: 746px; width: 947px; height: 7px; background: var(--white); }
  .band-coral { left: 0; top: 753px; width: 947px; height: 329px; background: var(--coral); }

  .deco-circle {
    left: 545px; top: 322px; width: 440px; height: 440px;
    border-radius: 50%; background: var(--orange);
    border: 4px solid var(--white);
  }

  .tag-your {
    left: 105px; top: 352px;
    font-family: "Oswald", sans-serif; font-weight: 200;
    font-size: 104px; line-height: 120px; color: var(--white);
  }
  .tag-strong {
    left: 107px; top: 468px;
    font-family: "Bebas Neue", sans-serif;
    font-size: 137px; line-height: 112px; color: var(--gold);
  }
  .tag-decisions {
    left: 106px; top: 808px;
    font-family: "Bebas Neue", sans-serif;
    font-size: 136px; line-height: 121px; color: #111;
  }

  /* photo section */
  .photo {
    left: 0; top: 1089px; width: 947px; height: 1048px;
    background: linear-gradient(160deg, #3a3f86 0%, #2f3274 45%, #24285e 100%);
  }

  .frame {
    border: 1px solid rgba(255,255,255,0.45); border-bottom: none;
  }
  .services-frame { left: 107px; top: 1224px; width: 728px; height: 116px; }
  .partners-frame { left: 111px; top: 1759px; width: 727px; height: 66px; }

  .pill {
    display: flex; align-items: center; justify-content: center;
    border-radius: 40px; text-transform: uppercase;
  }
  .services-title {
    left: 249px; top: 1189px; width: 449px; height: 71px;
    background: var(--white); color: #111;
    font-weight: 800; font-size: 36px;
  }
  .partners-title {
    left: 300px; top: 1732px; width: 340px; height: 53px;
    background: var(--coral); color: var(--white);
    font-weight: 700; font-size: 32px;
  }

  .service {
    width: 218px; height: 99px; background: var(--white);
    border-radius: 14px;
    display: flex; align-items: center; justify-content: center; text-align: center;
    font-size: 20px; line-height: 25px; color: #222; padding-top: 8px;
  }
  .service-icon {
    width: 54px; height: 54px; border-radius: 50%;
    background: var(--coral); border: 3px solid var(--indigo);
    display: flex; align-items: center; justify-content: center;
  }
  .service-icon svg { width: 30px; height: 30px; }

  .partner-badge {
    width: 135px; height: 54px; background: var(--white); border-radius: 12px;
  }

  .site {
    left: 111px; top: 2068px; width: 726px; height: 100px;
    background: var(--ink); border: 5px solid var(--white); border-radius: 50px;
    display: flex; align-items: center; justify-content: center;
    font-size: 37px; color: var(--white); letter-spacing: 0.3px;
  }
  .site b { font-weight: 600; }
</style>
</head>
<body>
<main class="banner">
  <!-- header -->
  <div class="abs brand-mark"></div>
  <div class="abs brand-name">Brightwave<br>Holdings</div>

  <!-- headline -->
  <div class="abs band-dark"></div>
  <div class="abs deco-circle"></div>
  <div class="abs band-gap"></div>
  <div class="abs band-coral"></div>
  <div class="abs tag-your">YOUR</div>
  <div class="abs tag-strong">TRUSTED<br>PARTNER</div>
  <div class="abs tag-decisions">IN DATA-DRIVEN<br>DECISIONS</div>

  <!-- photo area -->
  <div class="abs photo" role="img" aria-label="Photo of a professional analysing data on a large display, tinted in deep indigo"></div>

  <!-- services -->
  <div class="abs frame services-frame"></div>
  <div class="abs pill services-title">Our Services</div>

  <div class="abs service" style="left:107px;top:1339px;">Unified data,<br>analytics &amp; AI</div>
  <div class="abs service" style="left:364px;top:1339px;">Trusted insights,<br>faster outcomes</div>
  <div class="abs service" style="left:617px;top:1339px;">Real-time<br>intelligence<br>at scale</div>
  <div class="abs service" style="left:240px;top:1502px;">Clarity from<br>data complexity</div>
  <div class="abs service" style="left:492px;top:1502px;">Enterprise-ready,<br>secure solutions</div>

  <div class="abs service-icon" style="left:189px;top:1295px;">
    <svg viewBox="0 0 30 30" fill="none" stroke="#fff" stroke-width="2.4"><circle cx="15" cy="8" r="4"/><rect x="4" y="17" width="8" height="6"/><rect x="18" y="17" width="8" height="6"/><path d="M15 12v5M8 17v-2h14v2"/></svg>
  </div>
  <div class="abs service-icon" style="left:446px;top:1295px;">
    <svg viewBox="0 0 30 30" fill="none" stroke="#fff" stroke-width="2.4"><circle cx="15" cy="9" r="5"/><path d="M12.5 9l2 2 3-3.5M4 22l6-4 5 3 5-3 6 4"/></svg>
  </div>
  <div class="abs service-icon" style="left:699px;top:1295px;">
    <svg viewBox="0 0 30 30" fill="none" stroke="#fff" stroke-width="2.4"><circle cx="13" cy="15" r="8"/><path d="M21 10h5M21 15h5M21 20h5"/></svg>
  </div>
  <div class="abs service-icon" style="left:322px;top:1458px;">
    <svg viewBox="0 0 30 30" fill="none" stroke="#fff" stroke-width="2.4"><circle cx="11" cy="11" r="6"/><circle cx="19" cy="19" r="5"/><path d="M23 23l4 4"/></svg>
  </div>
  <div class="abs service-icon" style="left:574px;top:1458px;">
    <svg viewBox="0 0 30 30" fill="none" stroke="#fff" stroke-width="2.4"><path d="M6 13h18v12H6zM10 13V6M15 13V4M20 13V6"/></svg>
  </div>

  <!-- partners -->
  <div class="abs frame partners-frame"></div>
  <div class="abs pill partners-title">Our Partners</div>

  <div class="abs partner-badge" style="left:111px;top:1823px;"></div>
  <div class="abs partner-badge" style="left:259px;top:1823px;"></div>
  <div class="abs partner-badge" style="left:407px;top:1823px;"></div>
  <div class="abs partner-badge" style="left:555px;top:1823px;"></div>
  <div class="abs partner-badge" style="left:703px;top:1823px;"></div>
  <div class="abs partner-badge" style="left:184px;top:1897px;"></div>
  <div class="abs partner-badge" style="left:332px;top:1897px;"></div>
  <div class="abs partner-badge" style="left:479px;top:1897px;"></div>
  <div class="abs partner-badge" style="left:627px;top:1897px;"></div>

  <!-- web address -->
  <div class="abs site">www.<b>brightwave-holdings</b>.com</div>
</main>
</body>
</html>
```